Calorie website redesign while keeping current structure

****UPDATE****
Dear designers!

I'd really appreciate to see new color ideas.
The green-red-yellow scheme is the old scheme, and I want to change it. I asked for new colors with same structure, but I get designs with old colors and new structure. :(

My goal is to get a design with a good overall impression.
I need new color ideas where colors are in harmony and gives pleasant OVERALL impression to the eyes.

Your tools again:
1. you can use any colors (i prefer green and blue variations as the most dominant color)
2. you can use gradients
3. you can use transparency.
4. you can use background images.
5. you can change font type (but stay compatible with other languages like Hungarian)

All designs I got so far was not usable because they were not compatible with the site structure.
It was written in description we have fixed sizes, and what you can change and what you CANT change.

Note: i dont like white color. It looks empty and it doesnt give a character to the site.

Separation: it's important the site parts to be easily separated by the eye. The site consists of 4 main parts: menu, what did you eat, what did you do, and yellow calculation boxes. They should be separated easily by looking at it.
*****END OF UPDATE****

DEAR DESIGNERS!

My name is Zsolt, I run this website tornelviqa.hu which is the most popular calorie counting website in Hungary with 500.000 users. It has also an English version, fendrowix.com (started not long ago). Now you have to focus only on the mobile version main page:
https://fendrowix.com/?layout=m

There a lot of other urgent tasks about the site and I had no chance to improve the design in the last years . But I'm aware of the problem: the website doesn't look good enough to be appealing for new users. So now I decided to run a contest to see if you can help me with this.

UNDERSTANDING CURRENT DESIGN CONCEPT:

1. The original concept of the site was that calories are "bad" so they are red color, and sport activites are "good", so they are green color. Red and green is very different color (which is advantage in separating those sections), but they don't look nice together, so I'm ready to change the colors but somehow we still need to show that calories are "bad" and sports are "good". The yellow boxes are showing calculated numbers.
2. The original concept was that I wanted the whole site to have a "calculator feeling": the message is that it is not made to attract people by fancy design, but it's strongness is it's knowledge and usability, same as a hand calculator. I want to maintain this concept, but with a more modern design.
3. Another concept is that I want to make the usability easier for long time users instead of first time users. It means I prefer to show more options/buttons on the screen (which can be frightening to new users, but it's okay), instead of having a very easy-to-use feeling when you first visit our site (but later you need to click a lot to reach functions). Number one priority is still long time usability.
4. I want to emphasise I love to use colors to separate parts.

SUMMARY:

i know it's not easy to make it look better AND compatible current structure, it's a big challenge. Be creative and use your imaginations. It's possible that I will need further adjustments from winning designer in the future, so it's a plus if you will be available to work.

Thanks,
Zsolt Benkő
Updates

I got a car accident, and couldnt leave the countryside. i cant view and review works from here. I will send u an image tomorrow afternoon showing the fixed structure, to avoid misunderstandings in future. so far none of the design is usable, because they were NOT created in our 40px size/5px space structure as i requested in posting thanks for understanding

Received designs were not compatible with structure. It was written in the description, but now I also I updated the description to give a more clear view what I need.

Target Market(s)

weight-loss

Industry/Entity Type

Weight

Number of Pages Required

1 page

Font styles to use
Sans Serif

Colors

Designer to choose colors to be used in the design.

Requirements
Must have
• WHAT CHANGES AM I EXPECTING FROM YOU?
• 1. you can use new colors totally freely along all site.
• 2. You can add some color overlays, gradients, backgrounds, to different sections.
• 3. You can add new edges (delete /increase edges) to buttons/rows (without changing the size).
• 6. If you use new font, then it should be 100% compatible with different languages (for example: Hungarian characters like ö, ő, ü, ű, etc).
• 2. I need better design for input fields (currently inactive is red, and active is white, but you can change it)
• OTHER IMPORTANT NOTES:
• 1. Be careful with technologies which could cause performance issues, as site speed is very important.
• 2. The main goal now is NOT to get new images on buttons (it's perfectly okay if you dont touch them), but an overall better and consistent look. However if you want to achieve this goal by also redesigning buttons and rows (new color, new active/press effect, ), you can do this too. In current version buttons are 40x40, but in new design they will be 80x80.
• 3. The new color concept needs to be compatible with meal colors like breakfast, dinner, etc.
• 4. I love flat design, but I want to encourage you not to limit your imagination. I really appreciate creative ideas, flat or not.
• 5. I want a mobil app athmosphere. Most of the similar sites use so simple designs that they look like settings menu of your phone. I find them very boring, I want to separate sections with nice colors (maybe backgrounds).
• 6. Clear visibility is also important so try to avoid hurting it with too many new design elements.
• 7. First I need only a picture about the new design showing the main page with added meal rows. But of course in the end I need the winning design in a format which I we can use also to sub-menus and desktop version of the site.
Should not have
• WHAT YOU SHOULD NOT CHANGE:
• The menu structure, positions, the buttons sizes. The button animations and sub-menus are all based on this structure, where we use 5px spacing, and 40px rows, and buttons (however we want to double the resolution for these ones: 10 and 80px). We cannot change this basic structure, because it needs a lot of programming, so you need to be creative to make it look better with current structure.

```html
<!DOCTYPE html>
<html lang="en">
<head>
<meta charset="utf-8">
<title>Fendrowix – mobile main page</title>
<link href="https://fonts.googleapis.com/css2?family=Roboto:wght@300;400;500;700&display=swap" rel="stylesheet">
<style>
:root{
  --page:#ffffff;
  --blue:#0a86ff;
  --navy:#113056;
  --green:#00c98d;
  --green-bright:#0ee07a;
  --orange:#ff9a0a;
  --pink:#ff6fae;
  --red:#ff3b3b;
  --purple:#7b55e6;
  --panel:#1d2532;
  --row:#2b3544;
  --row-dark:#232c39;
  --nav:#1f2a38;
  --black:#0f141b;
  --teal-dark:#0b2a33;
  --teal-row:#123540;
  --text:#ffffff;
  --muted:#9aa6b6;
}
*{box-sizing:border-box;margin:0;padding:0}
html,body{width:1200px;height:994px;overflow:hidden;background:var(--page);font-family:'Roboto',sans-serif;color:var(--text)}
.stage{position:absolute;left:0;top:0;width:2100px;height:1740px;transform:scale(0.571429);transform-origin:0 0}
.abs{position:absolute}
.panel{position:absolute;overflow:hidden}

/* ---------- diary panel ---------- */
.diary{left:217px;top:136px;width:454px;height:1494px;background:var(--panel)}
.topbar{left:0;top:0;width:454px;height:62px;background:var(--blue)}
.brand-dot{left:12px;top:13px;width:36px;height:36px;border-radius:50%;background:#cfe6ff}
.brand-name{left:57px;top:22px;font-size:14px;line-height:16px;color:#e6f1ff}
.tab{top:21px;width:20px;height:20px;border-radius:50%;background:#5aaeff;font-size:11px;line-height:20px;text-align:center;font-weight:500}
.burger{left:413px;top:20px;width:24px;height:20px;border-top:2px solid #fff;border-bottom:2px solid #fff}
.burger::after{content:"";position:absolute;left:0;top:7px;width:24px;height:2px;background:#fff}
.datebar{left:0;top:62px;width:454px;height:75px;background:var(--nav)}
.today{left:0;width:454px;top:24px;text-align:center;font-size:26px;font-weight:300}
.kcalbar{left:0;top:137px;width:454px;height:57px;background:var(--black)}
.kcal-line{left:8px;top:10px;font-size:25px;font-weight:500;white-space:nowrap}
.kcal-line .eaten{color:var(--green)}
.kcal-line small{font-size:13px;font-weight:400;margin-left:4px}
.kcal-line small b{color:var(--green);font-weight:400}
.progress{left:2px;top:182px;width:450px;height:10px;border-radius:5px;background:#3a4350}
.progress i{position:absolute;left:0;top:0;width:302px;height:10px;border-radius:5px;background:var(--green)}
.input{background:#fff;color:#8a8f98;font-size:20px;font-weight:300}
.search-eat{left:6px;top:202px;width:374px;height:57px}
.search-eat span,.search-do span{position:absolute;left:47px;top:16px}
.search-btn{width:44px;height:44px;border-radius:50%}
.dots{width:55px;height:56px;background:var(--row-dark);display:flex;align-items:center;justify-content:center;gap:5px}
.dots i{width:5px;height:5px;border-radius:50%;background:#fff}
.dots.blue{background:var(--blue)}
.chip{height:17px;width:83px;background:var(--green);color:#0b2a20;font-size:10px;line-height:17px;text-align:center;white-space:nowrap;overflow:hidden}
.item{left:6px;width:312px;height:56px;background:var(--row)}
.item .name{position:absolute;left:19px;top:9px;font-size:20px;font-weight:400}
.item .qty{position:absolute;left:19px;top:31px;font-size:15px;color:#c0c7d2}
.kcal{position:absolute;right:8px;top:5px;text-align:right;font-size:26px;font-weight:500;line-height:27px}
.kcal em{display:block;font-style:normal;font-size:14px;font-weight:300;line-height:14px;color:#dde3ea}
.item .line{position:absolute;left:0;bottom:0;width:312px;height:4px}
.meal{left:116px;width:202px;height:56px}
.meal .name{position:absolute;left:15px;top:16px;font-size:20px;font-weight:500}
.macros{left:324px;width:57px;height:56px}
.macro{position:absolute;left:0;height:13px;width:57px;font-size:10px;font-weight:500}
.macro b{position:absolute;left:0;top:0;height:13px;border-radius:3px;font-weight:500;padding-left:3px;line-height:13px;color:#122}
.macro span{position:absolute;right:3px;top:0;line-height:13px}
.total{left:0;width:454px;height:63px;background:var(--black)}
.total .label{position:absolute;left:35px;top:19px;font-size:19px;font-weight:500}
.total .kcal{top:8px;right:142px;font-size:34px;line-height:32px}
.total.burn .kcal{right:79px}
.total .wedge{position:absolute;left:0;top:0;width:0;height:0;border-top:31px solid transparent;border-bottom:31px solid transparent;border-left:24px solid var(--green)}
.doband{left:0;top:1231px;width:454px;height:66px;background:var(--blue)}
.search-do{left:6px;top:4px;width:374px;height:57px}

/* ---------- nutrients panel ---------- */
.nutrients{left:832px;top:136px;width:455px;height:1407px;background:var(--teal-dark)}
.head{left:0;width:455px;height:64px;background:var(--green);font-size:19px;font-weight:500;line-height:64px;padding-left:36px;letter-spacing:.2px}
.head.blue{background:var(--blue)}
.chev{position:absolute;right:30px;top:27px;width:13px;height:13px;border-left:2px solid #fff;border-top:2px solid #fff;transform:rotate(45deg)}
.goal{left:10px;width:436px;height:52px;background:var(--teal-row)}
.goal .fill{position:absolute;left:0;top:0;height:52px}
.goal .val{position:absolute;left:0;width:420px;top:5px;text-align:center;font-size:19px;font-weight:500;line-height:22px}
.goal .val small{display:block;font-size:14px;font-weight:400}
.state{position:absolute;right:16px;top:12px;width:28px;height:28px;border-radius:50%}
.nrow{left:0;width:455px;height:30px}
.nrow .lab{position:absolute;right:212px;top:2px;font-size:21px;font-weight:400;white-space:nowrap}
.nrow .bar{position:absolute;left:255px;top:3px;width:193px;height:24px;background:var(--teal-row)}
.nrow .bar i{position:absolute;left:0;top:0;height:24px;background:var(--green)}
.nrow .num{position:absolute;left:0;top:-3px;width:100%;font-size:22px;font-weight:500;line-height:30px;padding-left:75px}
.outline-btn{border:1px solid var(--green);font-size:21px;font-weight:300;text-align:center}
.sq{width:56px;height:56px;background:var(--teal-row);display:flex;align-items:center;justify-content:center}
.sq.green{background:var(--green)}
.w-label{font-size:19px;font-weight:400;color:#e7eef2}
.w-sub{font-size:15px;color:#8ea3ad}

/* ---------- graphs panel ---------- */
.graphs{left:1464px;top:136px;width:455px;height:1047px;background:var(--teal-dark)}
.water{left:0;top:808px;width:455px;height:239px;background:var(--navy)}
.glass-art{left:56px;top:26px;width:60px;height:128px;background:linear-gradient(#2a4d76,#1c3d63);border-radius:6px}
.legend{font-size:11px;font-weight:500;line-height:18px}
.legend div{display:flex;align-items:center;gap:6px;background:#14353f;width:68px;margin-bottom:3px}
.legend i{width:17px;height:14px;display:inline-block}

/* ---------- add food panel ---------- */
.adder{left:1467px;top:1296px;width:472px;height:117px;background:var(--panel)}
.opt{top:81px;width:45px;height:31px;border:1px solid #3c4757;font-size:9px;line-height:10px;text-align:center;display:flex;align-items:center;justify-content:center}
.unit{top:42px;width:45px;height:34px;border:1px solid #3c4757;font-size:9px;line-height:10px;text-align:center;display:flex;align-items:center;justify-content:center}
</style>
</head>
<body>
<div class="stage">

<!-- ================= FOOD & ACTIVITY DIARY ================= -->
<section class="panel diary">
  <div class="abs topbar">
    <div class="abs brand-dot"></div>
    <div class="abs brand-name">Fendrowix</div>
    <div class="abs tab" style="left:174px">a</div>
    <div class="abs tab" style="left:214px">b</div>
    <div class="abs tab" style="left:254px">c</div>
    <div class="abs burger"></div>
  </div>

  <div class="abs datebar">
    <svg class="abs" style="left:26px;top:26px" width="14" height="22" viewBox="0 0 14 22"><path d="M12 2 3 11l9 9" fill="none" stroke="#1a8cff" stroke-width="2.5"/></svg>
    <div class="abs today">Today</div>
    <svg class="abs" style="left:331px;top:24px" width="22" height="24" viewBox="0 0 22 24"><rect x="2" y="4" width="18" height="18" rx="2" fill="none" stroke="#fff" stroke-width="2"/><path d="M2 10h18M7 1v6M15 1v6" stroke="#fff" stroke-width="2"/></svg>
    <svg class="abs" style="left:412px;top:26px" width="14" height="22" viewBox="0 0 14 22"><path d="m2 2 9 9-9 9" fill="none" stroke="#1a8cff" stroke-width="2.5"/></svg>
  </div>

  <div class="abs kcalbar">
    <div class="abs kcal-line"><span class="eaten">1500</span>/2500<small>you can eat <b>1000</b> more kcal today</small></div>
    <svg class="abs" style="left:408px;top:8px" width="28" height="28" viewBox="0 0 24 24"><path fill="#fff" d="M19.4 13a7.5 7.5 0 0 0 0-2l2.1-1.6-2-3.5-2.5 1a7 7 0 0 0-1.7-1L15 3h-4l-.4 2.9a7 7 0 0 0-1.7 1l-2.5-1-2 3.5L6.5 11a7.5 7.5 0 0 0 0 2l-2.1 1.6 2 3.5 2.5-1a7 7 0 0 0 1.7 1L11 21h4l.4-2.9a7 7 0 0 0 1.7-1l2.5 1 2-3.5zM13 15.5a3.5 3.5 0 1 1 0-7 3.5 3.5 0 0 1 0 7z"/></svg>
  </div>
  <div class="abs progress"><i></i></div>

  <div class="abs input search-eat">
    <svg class="abs" style="left:16px;top:20px" width="20" height="16" viewBox="0 0 20 16"><path d="M2 13h16M4 13a6 6 0 0 1 12 0M10 4v3" fill="none" stroke="#8a8f98" stroke-width="1.6"/></svg>
    <span>What did you eat?</span>
    <svg class="abs" style="left:298px;top:18px" width="20" height="20" viewBox="0 0 20 20"><path d="M2 3h16M2 8h11M2 13h7M2 18h4" stroke="#8a8f98" stroke-width="2"/></svg>
    <div class="abs search-btn" style="left:324px;top:6px;background:var(--green)">
      <svg width="44" height="44" viewBox="0 0 44 44"><circle cx="21" cy="21" r="8" fill="none" stroke="#fff" stroke-width="2.2"/><path d="m27 27 5 5" stroke="#fff" stroke-width="2.2"/></svg>
    </div>
  </div>
  <div class="abs dots" style="left:389px;top:202px"><i></i><i></i><i></i></div>

  <div class="abs chip" style="left:6px;top:271px">White bread</div>
  <div class="abs chip" style="left:96px;top:271px">Tomatoes</div>
  <div class="abs chip" style="left:186px;top:271px">Apples</div>
  <div class="abs chip" style="left:276px;top:271px">Grapes</div>
  <div class="abs chip" style="left:366px;top:271px">Potato</div>
  <div class="abs chip" style="left:6px;top:307px">Corn</div>
  <div class="abs chip" style="left:96px;top:307px">Pasta</div>
  <div class="abs chip" style="left:186px;top:307px">Protein bar</div>
  <div class="abs chip" style="left:276px;top:307px">Black beans...</div>
  <div class="abs chip" style="left:366px;top:307px">Egg</div>

  <!-- food rows -->
  <div class="abs item" style="top:337px"><div class="name">Cheese Sandwich</div><div class="qty">300 gr</div><div class="kcal">460<em>kcal</em></div><div class="line" style="background:var(--blue)"></div></div>
  <div class="abs meal" style="top:401px;background:var(--blue)"><div class="name">Breakfast</div><div class="kcal">460<em>kcal</em></div></div>
  <div class="abs item" style="top:465px"><div class="name">Apple</div><div class="qty">150 gr</div><div class="kcal">60<em>kcal</em></div><div class="line" style="background:var(--green)"></div></div>
  <div class="abs meal" style="top:529px;background:var(--green)"><div class="name">Mid-morning</div><div class="kcal">60<em>kcal</em></div></div>
  <div class="abs item" style="top:592px"><div class="name">Cesar Salad</div><div class="qty">300 gr</div><div class="kcal">150<em>kcal</em></div><div class="line" style="background:var(--orange)"></div></div>
  <div class="abs meal" style="top:656px;background:var(--orange)"><div class="name">Lunch</div><div class="kcal">150<em>kcal</em></div></div>
  <div class="abs item" style="top:720px"><div class="name">Grapes</div><div class="qty">200 gr</div><div class="kcal">130<em>kcal</em></div><div class="line" style="background:var(--pink)"></div></div>
  <div class="abs meal" style="top:784px;background:var(--pink)"><div class="name">Mid-afternoon</div><div class="kcal">130<em>kcal</em></div></div>
  <div class="abs item" style="top:847px"><div class="name">Pizza</div><div class="qty">300 gr</div><div class="kcal">500<em>kcal</em></div><div class="line" style="background:var(--red)"></div></div>
  <div class="abs meal" style="top:911px;background:var(--red)"><div class="name">Dinner</div><div class="kcal">500<em>kcal</em></div></div>
  <div class="abs item" style="top:975px"><div class="name">Cheese Sandwich</div><div class="qty">300 gr</div><div class="kcal">50<em>kcal</em></div><div class="line" style="background:var(--purple)"></div></div>
  <div class="abs item" style="top:1039px"><div class="name">Cheese Sandwich</div><div class="qty">300 gr</div><div class="kcal">50<em>kcal</em></div><div class="line" style="background:var(--purple)"></div></div>
  <div class="abs meal" style="top:1102px;background:var(--purple)"><div class="name">Snack</div><div class="kcal">100<em>kcal</em></div></div>

  <!-- macro columns and row menus -->
  <div class="abs macros" style="top:337px"><div class="macro" style="top:1px"><b style="width:16px;background:var(--green)">P:</b><span>10</span></div><div class="macro" style="top:22px"><b style="width:38px;background:var(--orange)">C:</b><span>50</span></div><div class="macro" style="top:43px"><b style="width:27px;background:var(--purple)">F:</b><span>35</span></div></div>
  <div class="abs dots" style="left:389px;top:337px"><i></i><i></i><i></i></div>
  <div class="abs macros" style="top:401px"><div class="macro" style="top:1px"><b style="width:16px;background:var(--green)">P:</b><span>10</span></div><div class="macro" style="top:22px"><b style="width:38px;background:var(--orange)">C:</b><span>50</span></div><div class="macro" style="top:43px"><b style="width:27px;background:var(--purple)">F:</b><span>35</span></div></div>
  <div class="abs dots" style="left:389px;top:401px"><i></i><i></i><i></i></div>
  <div class="abs macros" style="top:465px"><div class="macro" style="top:1px"><b style="width:16px;background:var(--green)">P:</b><span>10</span></div><div class="macro" style="top:22px"><b style="width:38px;background:var(--orange)">C:</b><span>50</span></div><div class="macro" style="top:43px"><b style="width:27px;background:var(--purple)">F:</b><span>35</span></div></div>
  <div class="abs dots" style="left:389px;top:465px"><i></i><i></i><i></i></div>
  <div class="abs macros" style="top:529px"><div class="macro" style="top:1px"><b style="width:16px;background:var(--green)">P:</b><span>10</span></div><div class="macro" style="top:22px"><b style="width:38px;background:var(--orange)">C:</b><span>50</span></div><div class="macro" style="top:43px"><b style="width:27px;background:var(--purple)">F:</b><span>35</span></div></div>
  <div class="abs dots" style="left:389px;top:529px"><i></i><i></i><i></i></div>
  <div class="abs macros" style="top:592px"><div class="macro" style="top:1px"><b style="width:16px;background:var(--green)">P:</b><span>10</span></div><div class="macro" style="top:22px"><b style="width:38px;background:var(--orange)">C:</b><span>50</span></div><div class="macro" style="top:43px"><b style="width:27px;background:var(--purple)">F:</b><span>35</span></div></div>
  <div class="abs dots" style="left:389px;top:592px"><i></i><i></i><i></i></div>
  <div class="abs macros" style="top:656px"><div class="macro" style="top:1px"><b style="width:16px;background:var(--green)">P:</b><span>10</span></div><div class="macro" style="top:22px"><b style="width:38px;background:var(--orange)">C:</b><span>50</span></div><div class="macro" style="top:43px"><b style="width:27px;background:var(--purple)">F:</b><span>35</span></div></div>
  <div class="abs dots" style="left:389px;top:656px"><i></i><i></i><i></i></div>
  <div class="abs macros" style="top:720px"><div class="macro" style="top:1px"><b style="width:16px;background:var(--green)">P:</b><span>10</span></div><div class="macro" style="top:22px"><b style="width:38px;background:var(--orange)">C:</b><span>50</span></div><div class="macro" style="top:43px"><b style="width:27px;background:var(--purple)">F:</b><span>35</span></div></div>
  <div class="abs dots" style="left:389px;top:720px"><i></i><i></i><i></i></div>
  <div class="abs macros" style="top:784px"><div class="macro" style="top:1px"><b style="width:16px;background:var(--green)">P:</b><span>10</span></div><div class="macro" style="top:22px"><b style="width:38px;background:var(--orange)">C:</b><span>50</span></div><div class="macro" style="top:43px"><b style="width:27px;background:var(--purple)">F:</b><span>35</span></div></div>
  <div class="abs dots" style="left:389px;top:784px"><i></i><i></i><i></i></div>
  <div class="abs macros" style="top:847px"><div class="macro" style="top:1px"><b style="width:16px;background:var(--green)">P:</b><span>10</span></div><div class="macro" style="top:22px"><b style="width:38px;background:var(--orange)">C:</b><span>50</span></div><div class="macro" style="top:43px"><b style="width:27px;background:var(--purple)">F:</b><span>35</span></div></div>
  <div class="abs dots" style="left:389px;top:847px"><i></i><i></i><i></i></div>
  <div class="abs macros" style="top:911px"><div class="macro" style="top:1px"><b style="width:16px;background:var(--green)">P:</b><span>10</span></div><div class="macro" style="top:22px"><b style="width:38px;background:var(--orange)">C:</b><span>50</span></div><div class="macro" style="top:43px"><b style="width:27px;background:var(--purple)">F:</b><span>35</span></div></div>
  <div class="abs dots" style="left:389px;top:911px"><i></i><i></i><i></i></div>
  <div class="abs macros" style="top:975px"><div class="macro" style="top:1px"><b style="width:16px;background:var(--green)">P:</b><span>10</span></div><div class="macro" style="top:22px"><b style="width:38px;background:var(--orange)">C:</b><span>50</span></div><div class="macro" style="top:43px"><b style="width:27px;background:var(--purple)">F:</b><span>35</span></div></div>
  <div class="abs dots" style="left:389px;top:975px"><i></i><i></i><i></i></div>
  <div class="abs macros" style="top:1039px"><div class="macro" style="top:1px"><b style="width:16px;background:var(--green)">P:</b><span>10</span></div><div class="macro" style="top:22px"><b style="width:38px;background:var(--orange)">C:</b><span>50</span></div><div class="macro" style="top:43px"><b style="width:27px;background:var(--purple)">F:</b><span>35</span></div></div>
  <div class="abs dots" style="left:389px;top:1039px"><i></i><i></i><i></i></div>
  <div class="abs macros" style="top:1102px"><div class="macro" style="top:1px"><b style="width:16px;background:var(--green)">P:</b><span>10</span></div><div class="macro" style="top:22px"><b style="width:38px;background:var(--orange)">C:</b><span>50</span></div><div class="macro" style="top:43px"><b style="width:27px;background:var(--purple)">F:</b><span>35</span></div></div>
  <div class="abs dots" style="left:389px;top:1102px"><i></i><i></i><i></i></div>

  <div class="abs total" style="top:1166px"><div class="wedge"></div><div class="label">TOTAL KCAL</div><div class="kcal">1500<em>kcal</em></div></div>
  <div class="abs macros" style="top:1166px"><div class="macro" style="top:1px"><b style="width:57px;background:var(--green)">P:</b><span>10</span></div><div class="macro" style="top:22px"><b style="width:57px;background:var(--orange)">C:</b><span>50</span></div><div class="macro" style="top:43px"><b style="width:57px;background:var(--purple)">F:</b><span>35</span></div></div>
  <div class="abs dots" style="left:389px;top:1166px"><i></i><i></i><i></i></div>

  <!-- activities -->
  <div class="abs doband">
    <div class="abs input search-do">
      <svg class="abs" style="left:14px;top:22px" width="24" height="12" viewBox="0 0 24 12"><path d="M1 6h22M4 2v8M7 3v6M17 3v6M20 2v8" stroke="#8a8f98" stroke-width="1.6"/></svg>
      <span>What did you do?</span>
      <div class="abs search-btn" style="left:324px;top:6px;background:var(--blue)">
        <svg width="44" height="44" viewBox="0 0 44 44"><circle cx="21" cy="21" r="8" fill="none" stroke="#fff" stroke-width="2.2"/><path d="m27 27 5 5" stroke="#fff" stroke-width="2.2"/></svg>
      </div>
    </div>
    <div class="abs dots blue" style="left:389px;top:5px"><i></i><i></i><i></i></div>
  </div>
  <div class="abs item" style="top:1301px;width:375px"><div class="name">Running</div><div class="qty">15 min</div><div class="kcal">350<em>kcal</em></div><div class="line" style="background:var(--blue);width:375px"></div></div>
  <div class="abs dots blue" style="left:389px;top:1301px"><i></i><i></i><i></i></div>
  <div class="abs item" style="top:1364px;width:375px"><div class="name">Riding bike</div><div class="qty">30 min</div><div class="kcal">450<em>kcal</em></div><div class="line" style="background:var(--blue);width:375px"></div></div>
  <div class="abs dots blue" style="left:389px;top:1364px"><i></i><i></i><i></i></div>
  <div class="abs total burn" style="top:1429px;height:65px"><div class="wedge" style="border-left-color:var(--blue);border-top-width:32px;border-bottom-width:32px"></div><div class="label">TOTAL KCAL BURN</div><div class="kcal">1500<em>kcal</em></div></div>
  <div class="abs dots blue" style="left:389px;top:1433px"><i></i><i></i><i></i></div>
</section>

<!-- ================= NUTRIENTS & WEIGHT ================= -->
<section class="panel nutrients">
  <div class="abs head" style="top:0">NUTRIENT RECOMENDATIONS<span class="chev"></span></div>

  <div class="abs goal" style="top:71px"><div class="fill" style="width:210px;background:var(--green-bright)"></div><div class="val">40 / 80<small>Min protein left to eat: 40 g</small></div>
    <svg class="state" viewBox="0 0 28 28" style="background:var(--green)"><path d="m8 14 4 4 8-9" fill="none" stroke="#fff" stroke-width="2.5"/></svg></div>
  <div class="abs goal" style="top:134px"><div class="fill" style="width:156px;background:var(--orange)"></div><div class="val">100 / 300<small>Min Carb left to eat: 200 g</small></div>
    <svg class="state" viewBox="0 0 28 28" style="background:#1b2a33;border:2px solid #394b55"><path d="M8 13h10" stroke="#fff" stroke-width="2.5"/></svg></div>
  <div class="abs goal" style="top:197px"><div class="fill" style="width:99px;background:var(--purple)"></div><div class="val">10 / 70<small>Min Fat left to eat: 60 g</small></div>
    <svg class="state" viewBox="0 0 28 28" style="background:var(--red)"><path d="m9 9 10 10M19 9 9 19" stroke="#fff" stroke-width="2.5"/></svg></div>

  <div class="abs nrow" style="top:277px"><div class="lab">Fiber:</div><div class="bar"><i style="width:70px"></i><div class="num">10 g</div></div></div>
  <div class="abs nrow" style="top:313px"><div class="lab">Sugars:</div><div class="bar"><i style="width:103px"></i><div class="num">50 g</div></div></div>
  <div class="abs nrow" style="top:348px"><div class="lab">Calc:</div><div class="bar"><i style="width:135px"></i><div class="num">350 mg</div></div></div>
  <div class="abs nrow" style="top:384px"><div class="lab">Iron:</div><div class="bar"><i style="width:70px"></i><div class="num">10 g</div></div></div>
  <div class="abs nrow" style="top:420px"><div class="lab">Magnesium:</div><div class="bar"><i style="width:103px"></i><div class="num">50 g</div></div></div>
  <div class="abs nrow" style="top:455px"><div class="lab">Phosphor:</div><div class="bar"><i style="width:135px"></i><div class="num">350 mg</div></div></div>
  <div class="abs nrow" style="top:491px"><div class="lab">Potassium:</div><div class="bar"><i style="width:70px"></i><div class="num">10 g</div></div></div>
  <div class="abs nrow" style="top:527px"><div class="lab">Sodium:</div><div class="bar"><i style="width:103px"></i><div class="num">50 g</div></div></div>
  <div class="abs nrow" style="top:562px"><div class="lab">Zinc:</div><div class="bar"><i style="width:135px"></i><div class="num">350 mg</div></div></div>
  <div class="abs nrow" style="top:598px"><div class="lab">C-vitamin:</div><div class="bar"><i style="width:70px"></i><div class="num">10 g</div></div></div>
  <div class="abs nrow" style="top:633px"><div class="lab">Tiamin:</div><div class="bar"><i style="width:103px"></i><div class="num">50 g</div></div></div>
  <div class="abs nrow" style="top:669px"><div class="lab">Riboflavin:</div><div class="bar"><i style="width:135px"></i><div class="num">350 mg</div></div></div>
  <div class="abs nrow" style="top:705px"><div class="lab">Niacin:</div><div class="bar"><i style="width:70px"></i><div class="num">10 g</div></div></div>
  <div class="abs nrow" style="top:740px"><div class="lab">B6-vitamin:</div><div class="bar"><i style="width:103px"></i><div class="num">50 g</div></div></div>
  <div class="abs nrow" style="top:776px"><div class="lab">Cholesterol:</div><div class="bar"><i style="width:135px"></i><div class="num">350 mg</div></div></div>
  <div class="abs nrow" style="top:811px"><div class="lab">Caffeine:</div><div class="bar"><i style="width:135px"></i><div class="num">350 mg</div></div></div>

  <div class="abs outline-btn" style="left:18px;top:865px;width:166px;height:40px;line-height:38px">What is this?</div>
  <div class="abs sq" style="left:393px;top:855px"><svg width="28" height="28" viewBox="0 0 24 24"><path fill="#fff" d="M19.4 13a7.5 7.5 0 0 0 0-2l2.1-1.6-2-3.5-2.5 1a7 7 0 0 0-1.7-1L15 3h-4l-.4 2.9a7 7 0 0 0-1.7 1l-2.5-1-2 3.5L6.5 11a7.5 7.5 0 0 0 0 2l-2.1 1.6 2 3.5 2.5-1a7 7 0 0 0 1.7 1L11 21h4l.4-2.9a7 7 0 0 0 1.7-1l2.5 1 2-3.5zM13 15.5a3.5 3.5 0 1 1 0-7 3.5 3.5 0 0 1 0 7z"/></svg></div>

  <div class="abs head" style="top:922px">YOUR WEIGHT<span class="chev"></span></div>
  <div class="abs w-label" style="left:16px;top:1003px">Your previous weight</div>
  <div class="abs w-sub" style="left:16px;top:1031px">298 days ago</div>
  <div class="abs" style="left:330px;top:997px;width:119px;height:53px;background:var(--teal-row);font-size:22px;text-align:center;line-height:53px">59 kg</div>
  <div class="abs w-label" style="left:16px;top:1075px">Your previous weight (kg)</div>
  <div class="abs" style="left:330px;top:1061px;width:119px;height:53px;background:#fff"></div>
  <div class="abs sq green" style="left:393px;top:1126px"><svg width="30" height="30" viewBox="0 0 30 30"><path d="M15 4v16M9 14l6 6 6-6M3 22v5h24v-5" fill="none" stroke="#fff" stroke-width="2"/></svg></div>
  <div class="abs" style="left:0;width:455px;top:1196px;text-align:center;font-size:20px;font-weight:500"><span style="color:var(--green)">- 1 kg</span> weight loss in total.</div>

  <div class="abs head" style="top:1230px">YOUR WEIGHT<span class="chev"></span></div>
  <div class="abs" style="left:20px;top:1320px;width:219px;height:38px;background:var(--green);font-size:22px;line-height:38px;padding-left:17px;font-weight:400">Add measurement</div>
  <div class="abs sq" style="left:323px;top:1307px;font-size:28px;font-weight:500">?</div>
  <div class="abs sq green" style="left:393px;top:1307px"><svg width="30" height="30" viewBox="0 0 30 30"><path d="M15 4v16M9 14l6 6 6-6M3 22v5h24v-5" fill="none" stroke="#fff" stroke-width="2"/></svg></div>
</section>

<!-- ================= GRAPHS & WATER ================= -->
<section class="panel graphs">
  <div class="abs head" style="top:0">GRAPH<span class="chev"></span></div>
  <svg class="abs" style="left:0;top:64px" width="455" height="314" viewBox="0 64 455 314">
    <g stroke="#2d4a55" stroke-width="1">
      <path d="M79 89H433M79 166H433M79 242H433M79 319H433M79 89V319M433 89V319M255 89V319"/>
    </g>
    <g fill="#7f949d" font-family="Roboto, sans-serif" font-size="15">
      <text x="26" y="94">90.00</text><text x="26" y="171">85.00</text><text x="26" y="247">80.00</text><text x="26" y="324">75.00</text>
      <text x="60" y="354">2.20</text><text x="239" y="354">4.26</text><text x="417" y="354">6.30</text>
    </g>
    <path d="M89 101C180 170 260 240 310 262C350 282 390 300 426 311" fill="none" stroke="var(--green)" stroke-width="3.5"/>
  </svg>

  <div class="abs head" style="top:378px">GRAPH<span class="chev"></span></div>
  <svg class="abs" style="left:56px;top:480px" width="200" height="200" viewBox="-100 -100 200 200">
    <path d="M0 0L-70.6-63.7A95 95 0 0 1 95 0Z" fill="var(--purple)"/>
    <path d="M0 0L95 0A95 95 0 0 1 -73.8 59.8Z" fill="var(--green-bright)"/>
    <path d="M0 0L-73.8 59.8A95 95 0 0 1 -70.6 -63.7Z" fill="var(--orange)"/>
    <g fill="#fff" font-family="Roboto, sans-serif" font-size="21" font-weight="700" text-anchor="middle">
      <text x="21" y="-37">38%</text><text x="21" y="56">38%</text><text x="-58" y="7">24%</text>
    </g>
  </svg>
  <div class="abs legend" style="left:349px;top:556px">
    <div><i style="background:var(--green-bright)"></i>Protein</div>
    <div><i style="background:var(--orange)"></i>Carbs</div>
    <div><i style="background:var(--purple)"></i>Fats</div>
  </div>

  <div class="abs head blue" style="top:744px">Water Consumption<span class="chev"></span></div>
  <div class="abs water">
    <div class="abs glass-art" role="img" aria-label="Drawing of water drops above a drinking glass"></div>
    <div class="abs" style="left:200px;top:21px;width:246px;height:55px;background:var(--blue);font-size:20px;font-weight:500;text-align:center;line-height:55px">+ 1 glass (200ml)</div>
    <div class="abs" style="left:200px;top:83px;width:246px;height:55px;border:1px solid var(--blue);font-size:20px;text-align:center;line-height:53px">0 ml</div>
    <div class="abs sq" style="left:391px;top:149px;background:#163a66"><svg width="28" height="28" viewBox="0 0 24 24"><path fill="#fff" d="M19.4 13a7.5 7.5 0 0 0 0-2l2.1-1.6-2-3.5-2.5 1a7 7 0 0 0-1.7-1L15 3h-4l-.4 2.9a7 7 0 0 0-1.7 1l-2.5-1-2 3.5L6.5 11a7.5 7.5 0 0 0 0 2l-2.1 1.6 2 3.5 2.5-1a7 7 0 0 0 1.7 1L11 21h4l.4-2.9a7 7 0 0 0 1.7-1l2.5 1 2-3.5zM13 15.5a3.5 3.5 0 1 1 0-7 3.5 3.5 0 0 1 0 7z"/></svg></div>
    <div class="abs" style="left:392px;top:209px;font-size:20px;font-weight:500;color:var(--blue)">reset</div>
  </div>
</section>

<!-- ================= ADD FOOD ROW ================= -->
<section class="panel adder">
  <div class="abs" style="left:10px;top:10px;font-size:17px">Sweet Corn (cooked)</div>
  <div class="abs" style="left:318px;top:4px;font-size:26px;font-weight:500">100<span style="font-size:14px;font-weight:300;margin-left:3px">kcal</span></div>
  <div class="abs macros" style="left:396px;top:4px;width:35px;height:30px">
    <div class="macro" style="top:0;width:35px;height:8px;font-size:6px"><b style="width:10px;height:8px;line-height:8px;background:var(--green)">P</b><span style="line-height:8px">10</span></div>
    <div class="macro" style="top:11px;width:35px;height:8px;font-size:6px"><b style="width:24px;height:8px;line-height:8px;background:var(--orange)">C</b><span style="line-height:8px">50</span></div>
    <div class="macro" style="top:22px;width:35px;height:8px;font-size:6px"><b style="width:17px;height:8px;line-height:8px;background:var(--purple)">F</b><span style="line-height:8px">35</span></div>
  </div>
  <svg class="abs" style="left:440px;top:12px" width="18" height="18" viewBox="0 0 18 18"><path d="m2 2 14 14M16 2 2 16" stroke="#fff" stroke-width="2.5"/></svg>
  <div class="abs" style="left:7px;top:50px;font-size:16px">How much?</div>
  <div class="abs" style="left:98px;top:42px;width:93px;height:34px;background:#fff;color:#222;font-size:15px;text-align:center;line-height:34px">1</div>
  <div class="abs unit" style="left:196px;background:var(--green);border-color:var(--green)">g</div>
  <div class="abs unit" style="left:247px">Piece<br>100g</div>
  <div class="abs unit" style="left:297px">Pounds<br>454g</div>
  <div class="abs dots" style="left:347px;top:42px;width:45px;height:34px;background:transparent;border:1px solid #3c4757;gap:4px"><i style="width:4px;height:4px"></i><i style="width:4px;height:4px"></i><i style="width:4px;height:4px"></i></div>
  <div class="abs" style="left:398px;top:42px;width:68px;height:70px;background:var(--green)"><svg width="68" height="70" viewBox="0 0 68 70"><path d="m19 36 11 11 20-24" fill="none" stroke="#fff" stroke-width="3"/></svg></div>
  <div class="abs" style="left:41px;top:86px;font-size:16px">When?</div>
  <div class="abs opt" style="left:98px">Breakfast</div>
  <div class="abs opt" style="left:147px">Mid-<br>morn</div>
  <div class="abs opt" style="left:196px;background:var(--orange);border-color:var(--orange)">Lunch</div>
  <div class="abs opt" style="left:247px">Mid-<br>aftern</div>
  <div class="abs opt" style="left:297px">Dinner</div>
  <div class="abs opt" style="left:347px">Snack</div>
</section>

</div>
</body>
</html>
```